Popup Banners - BrightCounsel - Legal Technology

- We need two banners (same style) designed with two different images and different text.

- The details of the printing requirements are attached, along with suggested images.

- The banners should share the same theme as our website www.brightcounsel.com.au

- The first banner would include our logo (attached), use the 'roads join' image (attached) in some way and text: New Opportunities - Where legal services and technology meet.

- The second banner would include our logo (attached), use the 'jigsaw' image (attached) in some way and use text: Legal Technology Strategy, Advice and Capability.

- Details on what are required from the Printer is attached also.

Target Market(s)

Legal Professionals

Industry/Entity Type

Information Technology

Font styles to use
Sans Serif

Requirements
Must have
• Our logo (attached), suggested text and the image mentioned for each.
Nice to have
• Professional and modern look
Should not have
• Cheap looking

```html
<!DOCTYPE html>
<html lang="en">
<head>
<meta charset="utf-8">
<title>BrightCounsel – Popup Banners</title>
<link href="https://fonts.googleapis.com/css2?family=Mulish:wght@300;400&display=swap" rel="stylesheet">
<style>
  :root {
    --stage: #000000;
    --paper: #ffffff;
    --ink: #3f3f3f;
    --ink-soft: #555555;
    --sky: #5bbdf0;
    --charcoal: #4a4a4a;
  }
  * { margin: 0; padding: 0; box-sizing: border-box; }
  html, body { width: 1059px; height: 1200px; overflow: hidden; background: var(--stage); }
  body { position: relative; font-family: "Mulish", "Avenir Next", sans-serif; }

  .banner {
    position: absolute;
    top: 117px;
    width: 385px;
    height: 959px;
    background: var(--paper);
    overflow: hidden;
  }
  .banner--jigsaw { left: 98px; }
  .banner--roads { left: 585px; }

  .banner__art { position: absolute; inset: 0; width: 385px; height: 959px; }

  .banner__headline {
    position: absolute;
    left: 0; right: 0;
    text-align: center;
    color: var(--ink);
    font-weight: 400;
    font-size: 38px;
  }
  .banner--jigsaw .banner__headline { top: 402px; line-height: 71px; }
  .banner--roads .banner__headline { top: 391px; line-height: 58px; }

  .brand {
    position: absolute;
    left: 0; right: 0;
    top: 703px;
    display: flex;
    justify-content: center;
    align-items: center;
    gap: 12px;
  }
  .brand__mark { width: 22px; height: 22px; background: var(--sky); }
  .brand__name {
    font-size: 29px;
    font-weight: 400;
    letter-spacing: 4px;
    color: var(--ink);
  }
  .brand__url {
    position: absolute;
    left: 0; right: 0;
    top: 756px;
    text-align: center;
    font-size: 18px;
    color: var(--ink-soft);
  }
</style>
</head>
<body>

<section class="banner banner--jigsaw">
  <svg class="banner__art" viewBox="0 0 385 959" xmlns="http://www.w3.org/2000/svg">
    <defs>
      <radialGradient id="jigsawTone" cx="0.6" cy="0.45" r="0.7">
        <stop offset="0" stop-color="#e8f4ff"/>
        <stop offset="0.25" stop-color="#5fa8ee"/>
        <stop offset="0.6" stop-color="#1d4f9c"/>
        <stop offset="1" stop-color="#0a1c45"/>
      </radialGradient>
    </defs>
    <path role="img" aria-label="Photo of a hand placing a glowing jigsaw puzzle piece" fill="url(#jigsawTone)"
      d="M0 0 H385 V190 C330 280 220 320 150 312 C80 306 30 280 0 250 Z"/>
    <path fill="var(--charcoal)" d="M0 250 C30 280 80 306 150 312 C220 320 330 280 385 190 V222 C330 300 220 334 150 330 C80 326 30 300 0 272 Z"/>
    <path fill="var(--sky)" d="M0 272 C30 300 80 326 150 330 C220 334 330 300 385 222 V244 C330 322 220 352 150 346 C80 341 30 316 0 288 Z"/>
    <path fill="var(--sky)" d="M0 900 C60 830 180 800 260 808 C320 816 360 846 385 876 V959 H0 Z"/>
    <path fill="var(--charcoal)" d="M0 916 C70 848 190 822 270 832 C330 842 365 872 385 900 V959 H0 Z"/>
    <path fill="var(--paper)" d="M0 934 C80 868 200 848 275 860 C325 870 360 905 372 959 H0 Z"/>
  </svg>
  <h2 class="banner__headline">Legal Technology<br>Strategy, Advice<br>and Capability.</h2>
  <div class="brand"><span class="brand__mark"></span><span class="brand__name">BrightCounsel</span></div>
  <p class="brand__url">www.brightcounsel.com.au</p>
</section>

<section class="banner banner--roads">
  <svg class="banner__art" viewBox="0 0 385 959" xmlns="http://www.w3.org/2000/svg">
    <defs>
      <linearGradient id="roadsTone" x1="0" y1="0" x2="0" y2="1">
        <stop offset="0" stop-color="#2d7fd0"/>
        <stop offset="0.22" stop-color="#9fd0f2"/>
        <stop offset="0.3" stop-color="#4c9a2e"/>
        <stop offset="0.7" stop-color="#3a8a22"/>
        <stop offset="1" stop-color="#1f5a14"/>
      </linearGradient>
    </defs>
    <path role="img" aria-label="Photo of two dirt roads joining across a green grassy hill under a blue sky" fill="url(#roadsTone)"
      d="M0 0 H385 V190 C330 280 220 320 150 312 C80 306 30 280 0 250 Z"/>
    <path fill="var(--charcoal)" d="M0 250 C30 280 80 306 150 312 C220 320 330 280 385 190 V222 C330 300 220 334 150 330 C80 326 30 300 0 272 Z"/>
    <path fill="var(--sky)" d="M0 272 C30 300 80 326 150 330 C220 334 330 300 385 222 V244 C330 322 220 352 150 346 C80 341 30 316 0 288 Z"/>
    <path fill="var(--sky)" d="M0 900 C60 830 180 800 260 808 C320 816 360 846 385 876 V959 H0 Z"/>
    <path fill="var(--charcoal)" d="M0 916 C70 848 190 822 270 832 C330 842 365 872 385 900 V959 H0 Z"/>
    <path fill="var(--paper)" d="M0 934 C80 868 200 848 275 860 C325 870 360 905 372 959 H0 Z"/>
  </svg>
  <h2 class="banner__headline">New Opportunities<br>- Where legal<br>services and<br>technology meet.</h2>
  <div class="brand"><span class="brand__mark"></span><span class="brand__name">BrightCounsel</span></div>
  <p class="brand__url">www.brightcounsel.com.au</p>
</section>

</body>
</html>
```